Real Estate Search Site Re-Design of 2 Pages

Looking for designs to optimize 2 pages of our current site design. Our site allows users to find properties to purchase or rent.

Basically there are 4 panes
1. The top red one where you actually type in what you''re looking for.
2. The map pane that shows the properties
3. The scrollable results pane.
4. Property details pane.

A typical search would go like this:
1. User fills in their search criteria in the top pane in red. Clicks Find Homes
2. Site updates the map with properties plotted that fit the criteria. Site also populates the results pane at the bottom. Site shows the most newest property that fits the search criteria on the right.
3. User will scroll through the results pane or the map and click a property.
4. Site will update the property details pane with information on the selected property.

Search/Results Page
This main page needs a search form area, a results area, an area to display details of a property selected, a map to show results, and an area to display a real estate agent's information. The design must be full-screen to use all the space on the screen. All information should fit on a 1366x768 screen size. Please see sample screen shot.

Property Details Page
This one can be fixed width of 978px. This page needs all the elements that are displayed in the sample PNG file. Ideally, we want to be able to see all important information without scrolling on a 1366x768 screen. The important information in this size are Pictures with controls, address, bedrooms, bathrooms, square feet, square feet of the lot, days on market, agent information, and buttons to request a showing or get more information.

Our Goal:
Our goal is to get create a different way to display the data in an effective way. We want different ways to show the search results, maybe a vertical, scrolling list of property information with pictures. Or even a horizontal scrolling results pane. It must contain:

1. A map of the results
2. A way to scroll through the search results (like we have currently in case someone wants to search/sort bedrooms or square footage)
3. A way to view details of the property
4. A way to display agent information/picture

There's a lot of good design work coming through. Thank you.

Perhaps review some other real estate sales sites for ideas on pane configuration. Example site links:
http://www.brovenly.com/homes/for_sale/?gclid=QmTr8k2-xw7HJd3P9Lq0VnE5ZB (brovenly.com)
http://www.pemoda.com/?sem=1.2.1.5.7.1.0.14&gclid=ZKwp42h-ty8NGRmX5BqeuLcHTD (Pemoda.com)
http://www.quivrent.com/map_search/results/i/ (quivrent.com)

Our goal for the redesign is to display the data in a more effective way. Either with a better flow, more pictures, more information, smoother search process. Please see the updated brief for details. The main idea is to show the data in the most effective way possible.

Project Deadline Extended
Reason: Still looking at different ideas for the search results. We are still open for fresh ideas.

Industry/Entity Type

Real Estate

Font styles to use
Sans Serif

Colors
eb1f27

```html
<!DOCTYPE html>
<html lang="en">
<head>
<meta charset="utf-8">
<title>Home Search – Results</title>
<link href="https://fonts.googleapis.com/css2?family=Arimo:wght@400;700&family=Roboto+Condensed:wght@700&display=swap" rel="stylesheet">
<style>
:root{
  --brand:#eb1f27;
  --brand-dark:#b0070f;
  --brand-deep:#a1050c;
  --ink:#555;
  --ink-soft:#666;
  --grey-head:#7a7a7a;
  --grey-btn:#767676;
  --marker:#6b6b6b;
  --row-alt:#f3f3f3;
  --panel:#eeeeee;
  --map:#e6e1d6;
  --white:#fff;
}
*{margin:0;padding:0;box-sizing:border-box}
html,body{width:1200px;height:1000px;overflow:hidden;background:var(--white)}
body{position:relative;font-family:"Arimo",Arial,sans-serif;color:var(--ink)}
.abs{position:absolute}

/* header */
.site-header{left:0;top:0;width:1200px;height:91px;background:linear-gradient(#d10f17,var(--brand-deep))}
.logo{left:11px;top:22px;width:104px;height:55px;background:var(--white);border-radius:3px;
  font:700 21px "Roboto Condensed",Arial,sans-serif;color:var(--brand);text-align:center;line-height:57px}
.main-nav a{position:absolute;top:49px;color:var(--white);font-size:16px;text-decoration:none;text-shadow:0 1px 1px rgba(0,0,0,.45)}
.lang{right:7px;top:54px;color:var(--white);font-size:11px;font-weight:700;word-spacing:2px}
.lang span{margin-right:14px}

/* search bar */
.search-bar{left:0;top:91px;width:1200px;height:54px;background:var(--brand);border-top:1px solid #f25a60}
.search-bar .label{position:absolute;top:18px;color:var(--white);font-size:16px;text-shadow:0 1px 1px rgba(0,0,0,.5)}
.search-input{position:absolute;left:95px;top:9px;width:188px;height:35px;background:var(--white);border-radius:3px}
.find-btn{position:absolute;left:296px;top:9px;width:133px;height:36px;background:#333;border-radius:3px;color:var(--white);
  font-size:12px;font-weight:700;line-height:36px;padding-left:37px}
.find-btn svg{position:absolute;left:12px;top:11px}
.select{position:absolute;top:11px;height:31px;background:var(--white);border-radius:3px;font-size:12px;color:var(--ink);line-height:31px;padding-left:10px}
.select::after{content:"";position:absolute;right:9px;top:13px;border:6px solid transparent;border-top:6px solid #444;border-bottom:0}

/* map */
.map{left:0;top:145px;width:861px;height:370px;background:linear-gradient(135deg,#ebe7dd,#e2ddd2 60%,#dcd8cc)}
.map-edge{left:1193px;top:145px;width:7px;height:370px;background:var(--map)}
.markers{left:0;top:145px;width:861px;height:370px}
.result-count{left:264px;top:467px;width:334px;height:39px;background:rgba(90,90,90,.85);border-radius:3px;
  color:var(--white);font-size:13px;text-align:center;line-height:39px}

/* results table */
.results{left:0;top:515px;width:861px;height:163px;border-bottom:1px solid #ddd}
.results table{border-collapse:collapse;width:842px;font-size:12px}
.results th{height:30px;background:var(--grey-head);color:var(--white);text-align:left;font-weight:700;font-size:12px}
.results td{height:26.5px;color:var(--ink)}
.results tr:nth-child(odd) td{background:var(--row-alt)}
.results tr.is-selected td{background:var(--brand);color:var(--white)}
.caret{display:inline-block;margin-left:6px;border:4px solid transparent;border-top:5px solid var(--white);border-bottom:0;vertical-align:middle}
.c1{padding-left:34px;width:266px}.c2{width:133px}.c3{width:98px}.c4{width:78px}.c5{width:82px}.c6{width:74px}.c7{width:69px}
.scrollbar{left:842px;top:545px;width:19px;height:133px;background:#f1f1f1;border:1px solid #ccc}
.scrollbar .thumb{position:absolute;left:2px;top:22px;width:13px;height:34px;background:#c8c8c8}
.scrollbar .up,.scrollbar .down{position:absolute;left:4px;border:5px solid transparent}
.scrollbar .up{top:3px;border-bottom:6px solid #aaa;border-top:0}
.scrollbar .down{bottom:3px;border-top:6px solid #aaa;border-bottom:0}

/* detail panel */
.detail{left:862px;top:145px;width:331px;height:533px;background:var(--white);border-left:1px solid #ddd;border-right:1px solid #ddd}
.detail-title{position:absolute;left:13px;top:14px;font-size:14px;font-weight:700;color:var(--ink-soft);line-height:18px}
.photo{position:absolute;left:13px;top:62px;width:302px;height:147px;background:linear-gradient(160deg,#9a9a96,#efefeb 40%,#d8d6d0 65%,#8f8a82)}
.photo-bar{position:absolute;left:13px;top:180px;width:302px;height:29px;background:rgba(70,70,70,.8);color:var(--white);font-size:13px;text-align:center;line-height:29px}
.photo-bar svg{position:absolute;top:8px}
.facts{position:absolute;left:13px;top:211px;width:302px;list-style:none;font-size:13px;color:var(--ink)}
.facts li{height:24px;line-height:24px;padding-left:18px}
.facts li:nth-child(even){background:var(--panel)}
.btn{position:absolute;top:362px;height:41px;color:var(--white);font-size:15px;text-align:center;line-height:38px;border-radius:2px}
.btn-primary{left:12px;width:147px;background:var(--brand);border-bottom:3px solid var(--brand-dark)}
.btn-secondary{left:167px;width:148px;background:var(--grey-btn);border-bottom:3px solid #555}
.agent{position:absolute;left:0;top:415px;width:329px;height:118px;background:var(--panel)}
.agent-photo{position:absolute;left:13px;top:14px;width:81px;height:91px;background:linear-gradient(#b9b4ac,#8d96a3)}
.agent-info{position:absolute;left:110px;top:13px;color:var(--ink-soft);font-size:13px;line-height:17px}
.agent-role{font-size:13px;text-transform:uppercase}
.agent-name{font-size:15px;font-weight:700;margin-top:3px}
.agent-lic{font-size:15px;margin-top:5px}

/* spec annotations */
.spec{font:700 19px "Roboto Condensed",Arial,sans-serif;color:#6f6f6f;letter-spacing:-.5px}
.rule{height:0;border-top:1px solid var(--brand)}
.cap{width:10px;height:22px;background:var(--brand)}
</style>
</head>
<body>

<header class="site-header abs">
  <div class="logo abs">LOGO</div>
  <nav class="main-nav">
    <a style="left:476px">Communities</a>
    <a style="left:625px">Locations</a>
    <a style="left:739px">Contact Us</a>
  </nav>
  <div class="lang abs"><span>LANGUAGE</span>EN | UK | CK</div>
</header>

<form class="search-bar abs">
  <span class="label" style="left:10px">Location</span>
  <div class="search-input"></div>
  <div class="find-btn">
    <svg width="14" height="14" viewBox="0 0 14 14"><circle cx="8.5" cy="5.5" r="4" fill="#ddd"/><path d="M5.5 8.5 1.5 12.5" stroke="#ddd" stroke-width="2.4" stroke-linecap="round"/></svg>
    FIND HOMES
  </div>
  <span class="label" style="left:475px">Type</span>
  <div class="select" style="left:523px;width:144px">Condo/Townhouse</div>
  <span class="label" style="left:689px">Price</span>
  <div class="select" style="left:738px;width:68px">$700k</div>
  <span class="label" style="left:835px">To</span>
  <div class="select" style="left:863px;width:77px">$700k</div>
  <span class="label" style="left:964px">Beds</span>
  <div class="select" style="left:1012px;width:54px">3+</div>
  <span class="label" style="left:1088px">Baths</span>
  <div class="select" style="left:1138px;width:54px">3+</div>
</form>

<div class="map abs" role="img" aria-label="Street map of the search area showing the matching properties"></div>
<svg class="markers abs" width="861" height="370" viewBox="0 0 861 370" aria-label="Property markers">
  <defs>
    <g id="pin">
      <path d="M0 14 -6 6 A13 13 0 1 1 6 6 Z" transform="translate(0,0)"/>
      <circle cx="0" cy="-3" r="13.5"/>
      <path d="M-7 -2 0 -9 7 -2 M-5 -3v7h3.5v-4h3v4H5v-7" fill="#fff" stroke="#fff" stroke-width="1" stroke-linejoin="round"/>
    </g>
  </defs>
  <g fill="var(--marker)">
    <use href="#pin" x="97" y="122"/>
    <use href="#pin" x="344" y="206"/>
    <use href="#pin" x="193" y="272"/>
    <use href="#pin" x="707" y="284"/>
    <use href="#pin" x="680" y="310"/>
    <use href="#pin" x="723" y="36"/>
  </g>
  <g fill="var(--brand)">
    <use href="#pin" x="501" y="103"/>
  </g>
</svg>
<div class="map-edge abs" role="img" aria-label="Map continues"></div>
<div class="result-count abs">Your Search Found 324 Results. Click to view detail</div>

<section class="results abs">
  <table>
    <thead>
      <tr>
        <th class="c1">Address</th>
        <th class="c2">City<i class="caret"></i></th>
        <th class="c3">Price<i class="caret"></i></th>
        <th class="c4">Beds<i class="caret"></i></th>
        <th class="c5">Baths<i class="caret"></i></th>
        <th class="c6">Sq.Ft<i class="caret"></i></th>
        <th class="c7">Sq.Ft<i class="caret"></i></th>
        <th>Day<i class="caret"></i></th>
      </tr>
    </thead>
    <tbody>
      <tr><td class="c1">1840 Alder Crest Avenue</td><td>Maple Heights</td><td>$1.200,000</td><td>4</td><td>2.5</td><td>1,814</td><td>$765</td><td>4</td></tr>
      <tr><td class="c1">1840 Alder Crest Avenue</td><td>Maple Heights</td><td>$1.200,000</td><td>4</td><td>2.5</td><td>1,814</td><td>$765</td><td>4</td></tr>
      <tr class="is-selected"><td class="c1">1840 Alder Crest Avenue</td><td>Maple Heights</td><td>$1.200,000</td><td>4</td><td>2.5</td><td>1,814</td><td>$765</td><td>4</td></tr>
      <tr><td class="c1">1840 Alder Crest Avenue</td><td>Maple Heights</td><td>$1.200,000</td><td>4</td><td>2.5</td><td>1,814</td><td>$765</td><td>4</td></tr>
      <tr><td class="c1">1840 Alder Crest Avenue</td><td>Maple Heights</td><td>$1.200,000</td><td>4</td><td>2.5</td><td>1,814</td><td>$765</td><td>4</td></tr>
    </tbody>
  </table>
</section>
<div class="scrollbar abs"><i class="up"></i><i class="thumb"></i><i class="down"></i></div>

<aside class="detail abs">
  <h2 class="detail-title">1840 Alder Crest Avenue<br>Maple Heights</h2>
  <div class="photo" role="img" aria-label="Property photo: patio with white umbrella beside the house"></div>
  <div class="photo-bar">
    <svg style="left:18px" width="8" height="14" viewBox="0 0 8 14"><path d="M7 1 1 7l6 6" fill="none" stroke="#ccc" stroke-width="1.4"/></svg>
    1/10
    <svg style="right:10px" width="8" height="14" viewBox="0 0 8 14"><path d="M1 1l6 6-6 6" fill="none" stroke="#ccc" stroke-width="1.4"/></svg>
  </div>
  <ul class="facts">
    <li>Listing Price &nbsp;- &nbsp;$2,388,000</li>
    <li>Bed - 3 &nbsp;| &nbsp;Baths - 3 &nbsp;| &nbsp;Built in - 2014</li>
    <li>Sq.Ft - 3,640 &nbsp;(Sq.Ft./$656)</li>
    <li>Sq.Ft Lot - 9,866</li>
    <li>25 Days of Market (#AR5528170)</li>
    <li>Country of Harbor Crest Realty</li>
  </ul>
  <div class="btn btn-primary">VIEW DETAILS</div>
  <div class="btn btn-secondary">VISIT HOME</div>
  <div class="agent">
    <div class="agent-photo" role="img" aria-label="Buyer's agent portrait"></div>
    <div class="agent-info">
      <div class="agent-role">Buyer’s Agent</div>
      <div class="agent-name">Mara Lindell</div>
      <div>(555) 014-2290</div>
      <div>mara@nestwell.com</div>
      <div class="agent-lic">BRE &nbsp;#00412875</div>
    </div>
  </div>
</aside>

<div class="cap abs" style="left:0;top:746px"></div>
<div class="rule abs" style="left:0;top:757px;width:1200px"></div>
<div class="cap abs" style="left:1193px;top:746px"></div>
<div class="spec abs" style="left:511px;top:744px;background:var(--white);padding:0 2px">1366x768</div>
<div class="spec abs" style="left:0;top:767px">TTER</div>
<div class="spec abs" style="left:1173px;top:767px">GUT</div>

<div class="rule abs" style="left:11px;top:829px;width:850px"></div>
<div class="spec abs" style="left:529px;top:816px;background:var(--white);padding:0 2px">978</div>

</body>
</html>
```